Product labels for new supplements business targeting high performing creative people

I need a label design for different supplements like Whey, BCAA, Melatonin etc. that I could customize for each use case separately.

The brand is called lanternfolk.life, and it would be the first design of the labels. We haven't sold any products yet, but the target audience is people with growth mindset, people who want to be as efficient as possible and are constantly looking to improve their lifestyle. As part of that, they are also working out, but don't know much about supplements yet. Mostly people between 20-34.

I don't have a too specific idea of the expected design, though it should be light, warm, smart and minimalist, maybe have some patterns. It should looks smart and clean (and expensive). Orange and golden might be the additional colors for white. I have attached the templates of some products that I plan to sell and also the logo of the brand.

Here's what I have used for inspiration:
Brands that I like and are somewhat similar in concept: https://www.vimqera.com/ (!!specially the way they
bring "how the product helps them" in focus, not "what the product is" & https://www.pobri.care/ &
https://www.selvoda.com/sport/ & https://en.kambelo.fr/ &
https://gridmarket.com/profiles/corawellhaldesign/designs/417586

Here's how different products look like: https://prodaxel.com/catalog

Target Market(s)

target audience is people with growth mindset, people who want to be as efficient as possible and are constantly looking to improve their lifestyle. As part of that, they are also working out, but don't know much about supplements yet. Mostly people between 20-34.

Industry/Entity Type

Supplements

Font styles to use
Sans Serif

Colors
FFC000
F8CF3A
FAE287
FDF2CF
FEFAEE
F0912C
F2A743
F7CA91
FBE8D2
FDF5EE
EE7325
F08F49
F5BC92
FAE3D3
FDF4ED

Requirements
Must have
• Clean, smart and minimalist design that can be applied for different products in different sizes, like Whey protein, BCAA, vitamins etc. available here: https://prodaxel.com/catalog
Nice to have
• Patterns, expensive look
Should not have
• Doodles, too many colors

```html
<!DOCTYPE html>
<html lang="en">
<head>
<meta charset="UTF-8">
<title>lanternfolk.life — Melatonin Label</title>
<link href="https://fonts.googleapis.com/css2?family=Montserrat:ital,wght@0,300;0,400;0,500;0,600;1,300&family=Raleway:wght@400&display=swap" rel="stylesheet">
<style>
  :root {
    --page-bg: #f6f6f6;
    --label-white: #ffffff;
    --label-mist: #ececec;
    --ink: #1f1f1f;
    --ember: #ee4a1e;
    --orange: #f07a1e;
    --orange-soft: #f5bc92;
    --ghost: rgba(0, 0, 0, 0.05);
  }
  * { margin: 0; padding: 0; box-sizing: border-box; }
  html, body {
    width: 1200px;
    height: 1200px;
    overflow: hidden;
    background: var(--page-bg);
  }
  .label {
    position: absolute;
    left: 222px;
    top: 40px;
    width: 756px;
    height: 1120px;
    background: radial-gradient(ellipse at 50% 45%, var(--label-mist) 0%, #f4f4f4 45%, var(--label-white) 80%);
    font-family: "Montserrat", sans-serif;
    overflow: hidden;
  }
  .brand {
    position: absolute;
    top: 212px;
    left: 0;
    width: 100%;
    display: flex;
    justify-content: center;
    align-items: center;
    gap: 14px;
  }
  .brand-dot {
    width: 18px;
    height: 18px;
    border-radius: 50%;
    background: var(--orange);
  }
  .brand-name {
    font-size: 56px;
    font-weight: 500;
    color: var(--ink);
    letter-spacing: 0.005em;
  }
  .sleep-motif {
    position: absolute;
    left: 128px;
    top: 620px;
    width: 490px;
    height: 480px;
    border-radius: 50%;
    background: radial-gradient(circle at 40% 50%, var(--ghost) 0%, rgba(0,0,0,0.025) 45%, rgba(0,0,0,0) 70%);
  }
  .product-name {
    position: absolute;
    top: 460px;
    left: 0;
    width: 100%;
    text-align: center;
    font-family: "Raleway", sans-serif;
    font-weight: 400;
    font-size: 112px;
    line-height: 1;
    color: var(--ember);
    letter-spacing: 0.005em;
  }
  .category-band {
    position: absolute;
    top: 588px;
    left: 149px;
    width: 465px;
    height: 39px;
    background: var(--orange);
    color: var(--label-white);
    font-size: 19px;
    font-weight: 500;
    letter-spacing: 0.42em;
    display: flex;
    align-items: center;
    justify-content: center;
    padding-left: 0.42em;
  }
  .dose {
    position: absolute;
    top: 950px;
    left: 0;
    width: 100%;
    text-align: center;
    font-size: 40px;
    font-weight: 500;
    color: var(--ink);
  }
  .benefits {
    position: absolute;
    top: 1022px;
    left: 214px;
    display: flex;
    align-items: center;
    gap: 10px;
  }
  .benefits-icon { width: 54px; height: 60px; }
  .benefits-list {
    list-style: none;
    font-size: 29px;
    font-weight: 300;
    font-style: italic;
    color: var(--orange);
    line-height: 1.25;
  }
  .count {
    position: absolute;
    left: 672px;
    top: 820px;
    width: 34px;
    height: 230px;
    display: flex;
    flex-direction: column;
    align-items: center;
    gap: 14px;
  }
  .count-text {
    writing-mode: vertical-rl;
    transform: rotate(180deg);
    font-size: 19px;
    font-weight: 500;
    letter-spacing: 0.06em;
    color: var(--orange);
  }
  .count-tablet { width: 26px; height: 26px; }
</style>
</head>
<body>
  <main class="label">
    <div class="sleep-motif" role="img" aria-label="Faint crescent moon with sleep letters as background motif"></div>

    <header class="brand">
      <span class="brand-dot"></span>
      <span class="brand-name">lanternfolk.life</span>
    </header>

    <h1 class="product-name">MELATONIN</h1>
    <div class="category-band">DIETARY SUPPLEMENT</div>

    <p class="dose">1 mg</p>

    <div class="benefits">
      <svg class="benefits-icon" viewBox="0 0 54 60" aria-hidden="true">
        <path d="M22 10 A22 22 0 1 0 46 42 A18 18 0 1 1 22 10 Z" fill="none" stroke="#1f1f1f" stroke-width="2.4" stroke-linejoin="round"/>
        <text x="26" y="18" font-family="Montserrat, sans-serif" font-size="9" font-weight="600" fill="#1f1f1f">z</text>
        <text x="33" y="21" font-family="Montserrat, sans-serif" font-size="8" font-weight="600" fill="#1f1f1f">z</text>
        <text x="40" y="18" font-family="Montserrat, sans-serif" font-size="9" font-weight="600" fill="#1f1f1f">z</text>
      </svg>
      <ul class="benefits-list">
        <li>Fall asleep faster</li>
        <li>Stay asleep longer</li>
      </ul>
    </div>

    <div class="count">
      <span class="count-text">60 TABLETS</span>
      <svg class="count-tablet" viewBox="0 0 26 26" aria-hidden="true">
        <circle cx="13" cy="13" r="12" fill="#f07a1e"/>
        <line x1="8" y1="18" x2="18" y2="8" stroke="#ffffff" stroke-width="1.6" stroke-linecap="round"/>
      </svg>
    </div>
  </main>
</body>
</html>
```